Managed IT Services Business Card + Stationary
Making Technology Work for Your Business
thank you for all the business card submissionns.
I'd like to note a change in the cellphone number to (916) 555-0173
I will try to review the submissions in more detail this evening.

```html
<!DOCTYPE html>
<html lang="en">
<head>
<meta charset="utf-8">
<title>Parallax Managed Services – Business Cards</title>
<link rel="stylesheet" href="https://fonts.googleapis.com/css2?family=Open+Sans:wght@400;600;700&display=swap">
<style>
  :root {
    --stage: #5b5b5d;
    --card: #ffffff;
    --red: #c8102e;
    --red-dark: #8e0a1f;
    --grey: #b9bcc0;
    --grey-light: #e3e4e6;
    --ink: #3a3a3a;
    --muted: #6a6a6a;
    --rule: #d6d6d6;
  }
  * { box-sizing: border-box; margin: 0; padding: 0; }
  html, body { width: 1200px; height: 852px; overflow: hidden; }
  body {
    background: var(--stage);
    font-family: "Open Sans", Arial, sans-serif;
    color: var(--ink);
    position: relative;
  }
  .card {
    position: absolute;
    width: 540px;
    height: 309px;
    background: var(--card);
    border-radius: 16px;
    overflow: hidden;
    box-shadow: 0 6px 18px rgba(0,0,0,.35);
  }
  .card--vertical-split { left: 50px; top: 100px; }
  .card--stacked { left: 610px; top: 440px; }

  .card__swoosh { position: absolute; left: 0; bottom: 0; width: 100%; height: 110px; }

  .brand { position: absolute; display: flex; align-items: center; gap: 12px; }
  .brand__dot { width: 46px; height: 46px; border-radius: 50%; background: var(--red); flex: none; }
  .brand__name {
    font-weight: 700; color: var(--red); line-height: 1.05;
    letter-spacing: 1px; text-transform: uppercase;
  }
  .brand__name span { display: block; }

  .card--vertical-split .brand { left: 22px; top: 92px; flex-direction: column; gap: 10px; width: 200px; }
  .card--vertical-split .brand__dot { width: 60px; height: 60px; }
  .card--vertical-split .brand__name { font-size: 25px; text-align: center; }
  .card--vertical-split .brand__name span + span { font-size: 12.5px; letter-spacing: 2.6px; }

  .divider { position: absolute; left: 240px; top: 30px; width: 1px; height: 170px; background: var(--rule); }

  .contact { position: absolute; font-size: 11px; line-height: 1.5; }
  .contact__name { font-size: 16px; font-weight: 700; color: var(--red); line-height: 1.2; }
  .contact__title { font-size: 11px; font-weight: 600; color: var(--ink); }
  .contact__address { margin-top: 14px; color: var(--muted); }
  .contact__list { list-style: none; margin-top: 12px; color: var(--muted); }
  .contact__list li { display: flex; align-items: center; gap: 7px; white-space: nowrap; }
  .contact__list svg { width: 11px; height: 11px; flex: none; fill: var(--red); }

  .card--vertical-split .contact { left: 256px; top: 30px; }

  .card--stacked .brand { left: 96px; top: 34px; }
  .card--stacked .brand__dot { width: 56px; height: 56px; }
  .card--stacked .brand__name { font-size: 34px; }
  .card--stacked .brand__name span + span { font-size: 15px; letter-spacing: 5px; }

  .card--stacked .headline { position: absolute; left: 60px; top: 126px; white-space: nowrap; }
  .card--stacked .headline .contact__name { display: inline; font-size: 16px; }
  .card--stacked .headline .contact__title { display: inline; font-size: 12px; margin-left: 4px; }
  .card--stacked .address { position: absolute; left: 60px; top: 158px; font-size: 11px; line-height: 1.6; color: var(--muted); }
  .card--stacked .contact__list { position: absolute; left: 330px; top: 152px; margin: 0; font-size: 11px; line-height: 1.6; }
</style>
</head>
<body>

<svg width="0" height="0" style="position:absolute">
  <defs>
    <symbol id="icon-phone" viewBox="0 0 24 24"><path d="M6.6 10.8a15.1 15.1 0 0 0 6.6 6.6l2.2-2.2a1 1 0 0 1 1-.25 11.4 11.4 0 0 0 3.6.57 1 1 0 0 1 1 1V20a1 1 0 0 1-1 1A17 17 0 0 1 3 4a1 1 0 0 1 1-1h3.5a1 1 0 0 1 1 1c0 1.25.2 2.45.57 3.6a1 1 0 0 1-.25 1z"/></symbol>
    <symbol id="icon-mobile" viewBox="0 0 24 24"><path d="M7 1h10a2 2 0 0 1 2 2v18a2 2 0 0 1-2 2H7a2 2 0 0 1-2-2V3a2 2 0 0 1 2-2zm0 3v14h10V4zm5 15.5a1.2 1.2 0 1 0 0 2.4 1.2 1.2 0 0 0 0-2.4z"/></symbol>
    <symbol id="icon-mail" viewBox="0 0 24 24"><path d="M2 5h20v14H2zm2 2v.5l8 5 8-5V7zm0 2.9V17h16V9.9l-8 5z"/></symbol>
    <symbol id="icon-web" viewBox="0 0 24 24"><circle cx="12" cy="12" r="10"/></symbol>
    <symbol id="swoosh" viewBox="0 0 540 110" preserveAspectRatio="none">
      <path d="M0 46 C140 78 330 70 540 20 L540 38 C330 86 140 92 0 62 Z" fill="var(--grey-light)"/>
      <path d="M0 58 C150 88 340 80 540 30 L540 44 C340 94 150 100 0 72 Z" fill="var(--grey)"/>
      <path d="M0 74 C160 100 350 92 540 44 L540 110 L0 110 Z" fill="var(--red)"/>
      <path d="M0 96 C170 110 360 104 540 70 L540 110 L0 110 Z" fill="var(--red-dark)" opacity=".55"/>
    </symbol>
  </defs>
</svg>

<article class="card card--vertical-split">
  <div class="brand">
    <span class="brand__dot"></span>
    <p class="brand__name"><span>Parallax</span><span>Managed Services</span></p>
  </div>
  <div class="divider"></div>
  <div class="contact">
    <p class="contact__name">Dana Whitfield</p>
    <p class="contact__title">Solutions Architect</p>
    <p class="contact__address">4480 Harbor Point Dr<br>Suite #310-42<br>Sacramento, CA 95815</p>
    <ul class="contact__list">
      <li><svg><use href="#icon-phone"/></svg>(916) 555-0142</li>
      <li><svg><use href="#icon-mobile"/></svg>(916) 555-0173</li>
      <li><svg><use href="#icon-mail"/></svg>dana@parallaxms.com</li>
      <li><svg><use href="#icon-web"/></svg>www.parallaxms.com</li>
    </ul>
  </div>
  <svg class="card__swoosh"><use href="#swoosh"/></svg>
</article>

<article class="card card--stacked">
  <div class="brand">
    <span class="brand__dot"></span>
    <p class="brand__name"><span>Parallax</span><span>Managed Services</span></p>
  </div>
  <p class="headline"><span class="contact__name">Dana Whitfield</span> <span class="contact__title">- Solutions Architect</span></p>
  <p class="address">4480 Harbor Point Dr<br>Suite #310-42<br>Sacramento, CA 95815</p>
  <ul class="contact__list">
    <li><svg><use href="#icon-phone"/></svg>(916) 555-0142</li>
    <li><svg><use href="#icon-mobile"/></svg>(916) 555-0173</li>
    <li><svg><use href="#icon-mail"/></svg>dana@parallaxms.com</li>
  </ul>
  <svg class="card__swoosh"><use href="#swoosh"/></svg>
</article>

</body>
</html>
```